Flyer Design for Meridian Guild of Reflective Counsellors and Therapists (MGRCT)

We need a new flyer designed for MGRCT. We want to attract new members @ a tradeshow. Counsellors and Psychotherapists looking for a professional association with which to align themselves where they feel @ home because they share similar values.We would like to use the colours and leaves from our website which is www.mgrct-example.org if possible or similar colours and the photo of the tree in bloom from Facebook "stillwaterandtherapy". As well as our logo (www.mgrct-example.org), the TOVRA (www.tovra-example.org) logo as well somewhere in the bottom corner the Harmony Assembly logo (www.harmonyassembly-example.org).

Target Market(s)

Psychotherapists and Counsellors

Industry/Entity Type

Mental Health

Colors
876aae
b7a5cd
e4daeb
cadf82
abd036
9bcb3b

Requirements
Must have
• Logo
Nice to have
• Warm inviting photo of lotus flower
Should not have
• No monks

```html
<!DOCTYPE html>
<html lang="en">
<head>
<meta charset="utf-8">
<title>MGRCT Flyer</title>
<link rel="stylesheet" href="https://fonts.googleapis.com/css2?family=Crimson+Text:wght@400;600;700&display=swap">
<style>
  :root {
    --ink: #2b2326;
    --footer-ink: #ffffff;
    --maple-deep: #b8232f;
    --maple: #d9485a;
    --blossom: #f1c3cc;
    --blossom-pale: #fbe9ec;
    --swoosh-mauve: #c4649a;
    --swoosh-pink: #eab0c8;
    --footer-red: #e2334d;
    --footer-edge: #f07a8c;
    --card: #ffffff;
    --badge: #c9503a;
  }
  html, body { margin: 0; padding: 0; }
  body {
    width: 848px; height: 1200px; overflow: hidden;
    background: #ffffff;
    font-family: "Crimson Text", Georgia, serif;
    color: var(--ink);
  }
  .flyer { position: relative; width: 848px; height: 1200px; overflow: hidden; }
  .photo-backdrop {
    position: absolute; inset: 0;
    background:
      linear-gradient(180deg, var(--maple-deep) 0%, var(--maple) 14%, var(--blossom) 30%, var(--blossom-pale) 55%, var(--blossom) 80%, var(--blossom-pale) 100%);
  }
  .shapes { position: absolute; inset: 0; }
  .brand-mark {
    position: absolute; left: 42px; top: 250px;
    display: flex; align-items: center; gap: 12px;
    font-size: 30px; font-weight: 400; color: #3a3a3a; letter-spacing: 1px;
  }
  .brand-mark .dot { width: 40px; height: 40px; border-radius: 50%; background: #3a3a3a; }
  .partner-name {
    position: absolute; left: 660px; top: 70px; width: 140px; text-align: center;
    font-size: 36px; font-weight: 600; color: #2c3a7a; letter-spacing: 2px;
  }
  .membership {
    position: absolute; left: 604px; top: 196px; width: 196px; height: 86px;
    background: var(--card); display: flex; align-items: center; gap: 10px; padding-left: 8px; box-sizing: border-box;
  }
  .membership .badge { width: 60px; height: 60px; background: var(--badge); flex: none; }
  .membership p { margin: 0; font-size: 13px; line-height: 1.2; color: #444; }
  .intro {
    position: absolute; right: 46px; top: 306px; width: 500px; margin: 0;
    text-align: right; font-size: 19px; line-height: 26px;
  }
  .section { position: absolute; left: 24px; width: 790px; }
  .section h2 { margin: 0 0 4px; font-size: 21px; font-weight: 700; letter-spacing: 0.3px; }
  .section ul { margin: 0; padding: 0 0 0 16px; font-size: 18.5px; line-height: 24px; }
  .section li { margin-bottom: 5px; padding-left: 4px; }
  .values { top: 424px; }
  .goals { top: 688px; }
  .contact {
    position: absolute; right: 34px; top: 1052px; margin: 0;
    text-align: right; color: var(--footer-ink); font-weight: 700; font-size: 20px; line-height: 26.5px;
  }
  .contact .abn { font-size: 13px; font-weight: 600; }
</style>
</head>
<body>
<main class="flyer">
  <div class="photo-backdrop" role="img" aria-label="Photograph of a red autumn maple tree beside a temple roof, fading into a soft pale wash behind the text"></div>

  <svg class="shapes" width="848" height="1200" viewBox="0 0 848 1200" aria-hidden="true">
    <path d="M600 0 C560 110 380 210 0 258 L0 1200 L848 1200 L848 0 Z" fill="#ffffff" opacity="0.72"/>
    <path d="M610 0 C580 90 560 140 560 200 L560 290 L848 290 L848 0 Z" fill="#ffffff" opacity="0.9"/>
    <path d="M0 262 C260 262 470 180 650 78 C520 200 300 305 0 330 Z" fill="var(--swoosh-mauve)"/>
    <path d="M0 330 C300 305 520 210 650 78 C560 230 320 340 0 348 Z" fill="var(--swoosh-pink)"/>
    <path d="M0 1010 C260 945 560 925 848 952 L848 1200 L0 1200 Z" fill="var(--footer-edge)"/>
    <path d="M0 1030 C260 968 560 950 848 972 L848 1200 L0 1200 Z" fill="var(--footer-red)"/>
  </svg>

  <div class="brand-mark"><span class="dot"></span>MGRCT</div>
  <div class="partner-name">TOVRA</div>
  <div class="membership">
    <span class="badge"></span>
    <p>Member of Harmony Assembly of NSW</p>
  </div>

  <p class="intro">MGRCT provides accreditation practices that will support the highest quality practice in Buddhist Counselling and Psychotherapy and work collaboratively and beneficially with other Buddhist and Counselling and Psychotherapy Organisations.</p>

  <section class="section values">
    <h2>SOME OF OUR VALUES...</h2>
    <ul>
      <li>We care about therapists</li>
      <li>We strive to be of service to our members and allthose we come into contact with humility, fairness, patience and compassion</li>
      <li>We value the ongoing need for education for therapists but we also value the balance between the mind, the body and the spirit, knowing that all those need to be nourished</li>
      <li>We work in warm, generous, spirited partnership with others and we are open to working within and across sectors to influence and co-develop initiatives.</li>
    </ul>
  </section>

  <section class="section goals">
    <h2>OUR GOALS...</h2>
    <ul>
      <li>To present Buddhism in a thorough way</li>
      <li>To explore and discuss dhamma and how it can improve the effectiveness of a therapist’s life</li>
      <li>To provide ongoing education in all aspects of Buddhism for mental<br>health professionals</li>
      <li>To develop a dynamic organisation that stays attuned to changes in Buddhism as<br>it is expressed in the West</li>
      <li>To develop a strong membership/community</li>
      <li>To develop a relevant and important voice in the community</li>
      <li>To develop a unique professional identity</li>
      <li>To encourage positive social change</li>
    </ul>
  </section>

  <p class="contact">
    MGRCT <span class="abn">ABN12 345 678 901</span><br>
    PO Box 4820 Lindell Harbour NSW 2999<br>
    www.stillwaterandtherapy.org<br>
    info@stillwaterandtherapy.org
  </p>
</main>
</body>
</html>
```